Business card design needed

We require business cards for our young and innovative construction team.

Our business is Birch Constructions and we have used Lime, Navy and white with our colours so far.

We would like business cards that show our passion for perfection and detail, communication and management.

Looking forward to seeing the deigns!!

Industry/Entity Type

Communication

Contact Information for Business Card

Dan Prewitt
Birch Constructions Pty Ltd
PO Box 712 Carrow Ridge NSW 2177
Mobile: 0471 263 908
Email: dprewitt@birchconstructions.com.au
Web: www.birchconstructions.com.au

```html
<!DOCTYPE html>
<html lang="en">
<head>
<meta charset="utf-8">
<title>Birch Constructions – Business Card</title>
<link rel="stylesheet" href="https://fonts.googleapis.com/css2?family=Open+Sans:wght@400;600;700&display=swap">
<style>
  :root {
    --navy: #2f3d6b;
    --navy-deep: #28345e;
    --lime: #8dc63f;
    --white: #ffffff;
    --ink-soft: #dfe4f2;
    --stage: #e9eaee;
  }
  * { box-sizing: border-box; margin: 0; padding: 0; }
  html, body {
    width: 1200px;
    height: 1024px;
    overflow: hidden;
    background: var(--stage);
    font-family: "Open Sans", Arial, sans-serif;
  }
  .sheet {
    width: 1200px;
    height: 1024px;
    display: flex;
    flex-direction: column;
    align-items: center;
    justify-content: center;
    gap: 56px;
  }
  .card {
    position: relative;
    width: 760px;
    height: 434px;
    overflow: hidden;
    box-shadow: 0 10px 28px rgba(20, 28, 60, 0.25);
  }

  /* Front */
  .card-front { background: var(--navy); }
  .front-top {
    position: absolute;
    inset: 0 0 auto 0;
    height: 190px;
    background: var(--white);
    display: flex;
    align-items: center;
    padding-left: 62px;
  }
  .front-divider {
    position: absolute;
    left: 0; right: 0;
    top: 190px;
    height: 7px;
    background: var(--lime);
  }
  .brand {
    display: flex;
    align-items: center;
    gap: 14px;
  }
  .brand-mark {
    width: 22px;
    height: 22px;
    background: var(--lime);
    flex: none;
  }
  .brand-name {
    font-weight: 600;
    font-size: 40px;
    letter-spacing: 0.5px;
    color: var(--navy);
  }
  .front-details {
    position: absolute;
    left: 62px;
    top: 226px;
    color: var(--ink-soft);
  }
  .person-name {
    font-weight: 700;
    font-size: 27px;
    color: var(--lime);
    margin-bottom: 8px;
  }
  .company-line, .address-line {
    font-size: 15px;
    line-height: 22px;
  }
  .contact-list {
    list-style: none;
    margin-top: 6px;
  }
  .contact-list li {
    display: flex;
    align-items: center;
    gap: 10px;
    font-size: 15px;
    line-height: 25px;
  }
  .contact-icon { width: 15px; height: 15px; flex: none; }

  /* Back */
  .card-back {
    background: radial-gradient(ellipse at 50% 45%, #364778 0%, var(--navy) 55%, var(--navy-deep) 100%);
    display: flex;
    flex-direction: column;
    align-items: center;
    justify-content: center;
  }
  .card-back .brand-name {
    color: var(--white);
    font-size: 50px;
  }
  .card-back .brand-mark { width: 26px; height: 26px; }
  .back-web {
    margin-top: 34px;
    font-size: 16px;
    letter-spacing: 0.4px;
    color: var(--ink-soft);
  }
</style>
</head>
<body>
<main class="sheet">

  <section class="card card-front" aria-label="Business card front">
    <div class="front-top">
      <div class="brand">
        <span class="brand-mark"></span>
        <span class="brand-name">Birch Constructions</span>
      </div>
    </div>
    <div class="front-divider"></div>

    <div class="front-details">
      <p class="person-name">Dan Prewitt</p>
      <p class="company-line">Birch Constructions Pty Ltd PO Box</p>
      <p class="address-line">712 Carrow Ridge NSW 2177</p>
      <ul class="contact-list">
        <li>
          <svg class="contact-icon" viewBox="0 0 16 16" aria-hidden="true">
            <path d="M4 1.5 6.2 4.4 5 6.2c.9 1.9 2.5 3.6 4.6 4.7l1.8-1.2L14.4 12l-1.2 2.3c-5.9-.4-11-5.5-11.4-11.4Z" fill="#8dc63f"/>
          </svg>
          <span>0471 263 908</span>
        </li>
        <li>
          <svg class="contact-icon" viewBox="0 0 16 16" aria-hidden="true">
            <rect x="1" y="3" width="14" height="10" rx="1" fill="#8dc63f"/>
            <path d="M1.5 3.8 8 9l6.5-5.2" fill="none" stroke="#2f3d6b" stroke-width="1.4"/>
          </svg>
          <span>dprewitt@birchconstructions.com.au</span>
        </li>
        <li>
          <svg class="contact-icon" viewBox="0 0 16 16" aria-hidden="true">
            <circle cx="8" cy="8" r="7" fill="#8dc63f"/>
            <g fill="none" stroke="#2f3d6b" stroke-width="1.1">
              <ellipse cx="8" cy="8" rx="3" ry="6.5"/>
              <path d="M1.5 8h13M2.6 4.8h10.8M2.6 11.2h10.8"/>
            </g>
          </svg>
          <span>www.birchconstructions.com.au</span>
        </li>
      </ul>
    </div>
  </section>

  <section class="card card-back" aria-label="Business card back">
    <div class="brand">
      <span class="brand-mark"></span>
      <span class="brand-name">Birch Constructions</span>
    </div>
    <p class="back-web">www.birchconstructions.com.au</p>
  </section>

</main>
</body>
</html>
```